i would like a business card to leave with customers and potential customers for electrical work and for the supply and install of reverse cycle airconditioning in the domestic and commercial market.
I own my own business and im a sole trader. I have an a'class electrical lisence and also a refrigeration lisence so i am
able to offer complete installations in airconditioning by a fully qualified and lisenced tradesman.
im looking for something that comes across as unique and professional.
i had the coluor black and some gold in mind but open to any coluors.
something like Beacon Electrical & Refrigeration
or Beacon Air.
i will use this design on a business card to advertise through summer to help generate installs through the busy season.

Target Market(s)

Mainly domestic house holds through summer who are in need of airconditioning and reliable information to acomadate thier cooling and heating requirements

Industry/Entity Type

Electrical

Requirements
Must have
• Business name- Beacon
My name- Peter Wollaston
My mobile no- 0457 819 302
My email- prwollaston@tarvel.com.au
Installation & Decomissioning of aiconditioning split systems
LIC NO: KTR 407516
Nice to have
• Beacon Electrical & Refrigeration

```html
<!DOCTYPE html>
<html lang="en">
<head>
<meta charset="utf-8">
<title>Beacon Electrical &amp; Refrigeration – Business Card</title>
<link href="https://fonts.googleapis.com/css2?family=Aldrich&family=Arimo:wght@700&family=Source+Code+Pro:wght@600;700&display=swap" rel="stylesheet">
<style>
  :root {
    --gold-dark: #9a6a08;
    --gold-light: #c79a12;
    --black: #000;
    --white: #fff;
    --lime: #99ff00;
    --cyan: #00ffff;
    --grey: #555;
    --ink: #111;
  }
  * { margin: 0; padding: 0; box-sizing: border-box; }
  html, body { width: 927px; height: 1200px; overflow: hidden; }
  body {
    position: relative;
    background: linear-gradient(90deg, var(--gold-dark), var(--gold-light) 30%, var(--gold-dark) 60%, var(--gold-light));
    font-family: "Aldrich", sans-serif;
  }
  .side-label {
    position: absolute;
    left: 16px;
    font-family: "Arimo", sans-serif;
    font-weight: 700;
    font-size: 22px;
    color: var(--white);
    transform: translate(-50%, -50%) rotate(-90deg);
    white-space: nowrap;
  }
  .side-label--front { top: 244px; }
  .side-label--back { top: 844px; }

  .card { position: absolute; left: 41px; width: 849px; height: 520px; background: var(--black); overflow: hidden; }
  .card--front { top: 26px; }
  .card--back { top: 581px; height: 518px; }

  .front-lines { position: absolute; inset: 0; }
  .front-name {
    position: absolute; left: 327px; top: 254px;
    transform: translate(-50%, -50%);
    font-size: 84px; color: var(--lime); line-height: 1;
  }
  .licence-strip {
    position: absolute; left: 727px; top: 0; width: 57px; height: 100%;
    background: var(--grey);
  }
  .licence-strip span {
    position: absolute; left: 50%; top: 50%;
    transform: translate(-50%, -50%) rotate(-90deg);
    white-space: nowrap; font-size: 17px; color: var(--ink);
  }

  .back-panel { position: absolute; left: 0; top: 0; width: 849px; height: 291px; background: var(--white); }
  .back-frame { position: absolute; left: 21px; top: 20px; width: 807px; height: 280px; border: 3px solid var(--black); border-bottom: none; }
  .badge { position: absolute; left: 41px; top: 42px; width: 99px; height: 95px; background: var(--cyan); }
  .holder-name { position: absolute; right: 44px; top: 30px; font-size: 72px; color: var(--black); line-height: 1; }
  .contact { position: absolute; right: 44px; font-family: "Source Code Pro", monospace; font-weight: 600; color: var(--black); }
  .contact--phone { top: 128px; font-size: 23px; letter-spacing: 0.36em; margin-right: -0.36em; font-weight: 700; }
  .contact--email { top: 173px; font-size: 23px; }
  .contact--licence { top: 220px; font-size: 23px; color: var(--lime); }
  .icon { position: absolute; }
  .icon--phone { left: 427px; top: 105px; }
  .icon--mail { left: 425px; top: 173px; }

  .services {
    position: absolute; left: 0; top: 291px; width: 100%; height: 128px;
    color: var(--white); text-align: center; font-size: 37px; line-height: 42px; padding-top: 18px;
  }
  .trade-band {
    position: absolute; left: 0; top: 419px; width: 100%; height: 54px;
    background: var(--grey); color: var(--ink); text-align: center; font-size: 41px; line-height: 54px;
  }
</style>
</head>
<body>
  <div class="side-label side-label--front">FRONT</div>
  <div class="side-label side-label--back">BACK</div>

  <section class="card card--front">
    <svg class="front-lines" width="849" height="520" viewBox="0 0 849 520" aria-hidden="true">
      <g fill="none" stroke="#fff" stroke-width="4">
        <path d="M111 0 L0 310"/>
        <path d="M449 0 L666 76 Q700 92 690 124 L543 520"/>
        <path d="M0 444 L223 520"/>
      </g>
    </svg>
    <div class="front-name">Beacon</div>
    <div class="licence-strip"><span>[A'Class Electrical &amp; Refrigeration Liscense]</span></div>
  </section>

  <section class="card card--back">
    <div class="back-panel">
      <div class="back-frame"></div>
      <div class="badge" aria-hidden="true"></div>
      <h1 class="holder-name">Peter Wollaston</h1>

      <svg class="icon icon--phone" width="30" height="58" viewBox="0 0 30 58" aria-hidden="true">
        <g fill="none" stroke="#000" stroke-width="1.6">
          <rect x="3" y="12" width="20" height="42" rx="4"/>
          <line x1="8" y1="12" x2="8" y2="1"/>
          <rect x="7" y="17" width="12" height="8"/>
          <rect x="7" y="29" width="12" height="16"/>
        </g>
      </svg>
      <div class="contact contact--phone">0457 819 302</div>

      <svg class="icon icon--mail" width="33" height="24" viewBox="0 0 33 24" aria-hidden="true">
        <rect x="0" y="0" width="33" height="24" fill="#000"/>
        <path d="M1 1 L16.5 13 L32 1 M1 23 L12 10 M32 23 L21 10" stroke="#fff" stroke-width="1.6" fill="none"/>
      </svg>
      <div class="contact contact--email">prwollaston@tarvel.com.au</div>

      <div class="contact contact--licence">LIC NO: KTR 407516</div>
    </div>

    <p class="services">Installation &amp; Decommissioning<br>Split Systems</p>
    <p class="trade-band">Beacon Electrical &amp; Refrigeration</p>
  </section>
</body>
</html>
```